Web Developer Needs a Business Card Design

I need a personal business card design that represents me as a web developer for potential employers. I would like the background to be a dark color on the front for contrast with my logo and name. The back will have all my information along with a smaller version of the logo. I want something with a modern look and feel, not too conservative. This will be used for potential employers and freelance work.

Industry/Entity Type

Business

Contact Information for Business Card

Front should have my logo and name. The back should have all my personal information which would include: name: Tom Brevardi, phone: 570-614-9083, email: tombrevardi@mailwisp.com, website url: www.tombrevardi.com, logo, web developer.

Font styles to use
Sans Serif

Requirements
Must have
• Must include my logo. The color palette base color will be the logo color.

```html
<!DOCTYPE html>
<html lang="en">
<head>
<meta charset="UTF-8">
<title>Tom Brevardi – Business Card</title>
<link rel="stylesheet" href="https://fonts.googleapis.com/css2?family=Open+Sans:wght@400;700&display=swap">
<style>
  :root {
    --teal: #86c9b7;
    --charcoal: #333333;
    --paper: #ffffff;
    --backdrop: #dcdcdc;
    --shadow: rgba(0, 0, 0, 0.22);
  }
  * { margin: 0; padding: 0; box-sizing: border-box; }
  html, body {
    width: 1200px;
    height: 900px;
    overflow: hidden;
  }
  body {
    background: var(--backdrop);
    font-family: "Open Sans", Arial, sans-serif;
    position: relative;
  }
  .card {
    position: absolute;
    left: 300px;
    width: 600px;
    height: 343px;
    overflow: hidden;
    box-shadow: 0 8px 24px var(--shadow);
  }

  /* Front: white face with logo and name */
  .card--front {
    top: 60px;
    background: var(--paper);
  }
  .card--front .band-teal {
    position: absolute; top: 0; left: 0; right: 0;
    height: 26px; background: var(--teal);
  }
  .card--front .band-dark {
    position: absolute; top: 26px; left: 0; right: 0;
    height: 26px; background: var(--charcoal);
  }
  .front-content {
    position: absolute;
    top: 86px; left: 0; right: 0;
    display: flex; flex-direction: column; align-items: center;
  }
  .logo-mark {
    display: flex; align-items: center; justify-content: center;
    border: 6px solid var(--teal);
    border-radius: 50%;
    color: var(--teal);
    font-weight: 700;
    text-align: center;
    line-height: 1.1;
  }
  .card--front .logo-mark {
    width: 122px; height: 122px;
    font-size: 15px;
  }
  .front-name {
    margin-top: 20px;
    color: var(--teal);
    font-weight: 700;
    font-size: 31px;
    letter-spacing: 0.5px;
    line-height: 1;
  }
  .front-role {
    margin-top: 8px;
    color: var(--charcoal);
    font-size: 15px;
    letter-spacing: 0.3px;
  }

  /* Back: dark face with contact details */
  .card--back {
    top: 477px;
    background: var(--charcoal);
  }
  .card--back .band-white-top {
    position: absolute; top: 0; left: 0; right: 0;
    height: 14px; background: var(--paper);
  }
  .card--back .band-teal {
    position: absolute; top: 14px; left: 0; right: 0;
    height: 30px; background: var(--teal);
  }
  .card--back .band-white-bottom {
    position: absolute; top: 44px; left: 0; right: 0;
    height: 20px; background: var(--paper);
  }
  .card--back .logo-mark {
    position: absolute;
    left: 34px; top: 118px;
    width: 136px; height: 136px;
    font-size: 16px;
  }
  .back-details {
    position: absolute;
    left: 196px; top: 118px;
  }
  .back-headline {
    display: flex; align-items: baseline; gap: 22px;
    white-space: nowrap;
  }
  .back-name {
    color: var(--teal);
    font-weight: 700;
    font-size: 26px;
    letter-spacing: 1px;
  }
  .back-role {
    color: var(--paper);
    font-size: 15px;
    letter-spacing: 0.4px;
  }
  .contact-list {
    margin-top: 6px;
    display: grid;
    grid-template-columns: 68px auto;
    row-gap: 2px;
    font-size: 15px;
    line-height: 1.45;
  }
  .contact-label { color: var(--teal); }
  .contact-value { color: var(--paper); }
</style>
</head>
<body>

  <section class="card card--front" aria-label="Business card front">
    <div class="band-teal"></div>
    <div class="band-dark"></div>
    <div class="front-content">
      <div class="logo-mark">TOM<br>BREVARDI</div>
      <h1 class="front-name">TOM BREVARDI</h1>
      <p class="front-role">WEB DEVELOPER</p>
    </div>
  </section>

  <section class="card card--back" aria-label="Business card back">
    <div class="band-white-top"></div>
    <div class="band-teal"></div>
    <div class="band-white-bottom"></div>
    <div class="logo-mark">TOM<br>BREVARDI</div>
    <div class="back-details">
      <div class="back-headline">
        <h2 class="back-name">TOM BREVARDI</h2>
        <span class="back-role">// &nbsp;WEB DEVELOPER</span>
      </div>
      <dl class="contact-list">
        <dt class="contact-label">Mobile</dt>
        <dd class="contact-value">570-614-9083</dd>
        <dt class="contact-label">Email</dt>
        <dd class="contact-value">tombrevardi@mailwisp.com</dd>
        <dt class="contact-label">Website</dt>
        <dd class="contact-value">www.tombrevardi.com</dd>
      </dl>
    </div>
  </section>

</body>
</html>
```